Flyer-Design für Tierphysiotherapie und Osteopathie
Zielgruppe
Tierphysiotherapie und Osteopathie Lotte Brenner
Aufgabenstellung
Text des gewünschten Flyers ist hochgeladen.
Ebenso die Visitenkarten und das Logo, sowie die Website - zur Orientierung von Farben, Schriftarten, etc.
Auch ein paar Bilder sind beigefügt.

```html
<!DOCTYPE html>
<html lang="de">
<head>
<meta charset="utf-8">
<title>Flyer Tierphysiotherapie Lotte Brenner</title>
<link href="https://fonts.googleapis.com/css2?family=Baloo+2:wght@600;700&family=Catamaran:wght@400;600;700&display=swap" rel="stylesheet">
<style>
:root{
  --yellow:#f0b323;
  --ink:#2b2b2b;
  --paper:#ffffff;
  --bg:#f6f6f6;
  --photo-barn:linear-gradient(135deg,#6b6158 0%,#8a5a3a 45%,#c0673a 70%,#3aa6a6 100%);
  --photo-meadow:linear-gradient(160deg,#cfd6c8 0%,#a06a3e 40%,#5f8f3c 75%,#3f6f2a 100%);
  --photo-grass:linear-gradient(170deg,#6b8f4a 0%,#8aa86a 45%,#56703f 100%);
}
*{box-sizing:border-box;margin:0;padding:0}
html,body{width:1200px;height:817px;overflow:hidden;background:var(--bg)}
body{position:relative;font-family:"Catamaran",sans-serif;color:var(--ink)}
.flyer{position:absolute;top:14px;width:370px;height:790px;background:var(--paper);overflow:hidden;box-shadow:0 3px 12px rgba(0,0,0,.12)}
.flyer--front{left:190px}
.flyer--back{left:640px}
.heading{font-family:"Baloo 2",sans-serif;font-weight:700}

/* front */
.front-shapes{position:absolute;inset:0}
.front-photo-fill{position:absolute;left:0;top:0;width:370px;height:320px;background:var(--photo-barn);clip-path:polygon(0 0,100% 0,100% 73%,0 97%)}
.name-box{position:absolute;right:0;top:232px;width:178px;height:86px;background:var(--yellow);border-radius:34px 0 0 34px;border:5px solid var(--paper);border-right:none;color:var(--paper);text-align:center;padding-top:6px;line-height:1.02}
.name-box .name{font-size:22px}
.name-box .role{font-size:18px}
.wish-title{position:absolute;left:30px;top:336px;font-size:22px;color:var(--yellow)}
.wish-list{position:absolute;left:30px;top:372px;width:320px;list-style:none}
.wish-list li{position:relative;padding-left:24px;font-size:12px;line-height:1.3;margin-bottom:12px}
.tick{position:absolute;left:0;top:1px;width:16px;height:16px}
.closing{position:absolute;left:36px;top:615px;font-size:30px;line-height:1.05;color:var(--yellow)}

/* back */
.intro-bar{position:absolute;left:0;top:22px;width:330px;height:62px;background:var(--yellow);border-radius:0 14px 14px 0;color:var(--paper);font-size:14.5px;line-height:1.2;padding:8px 10px 0 18px}
.intro-text{position:absolute;left:18px;top:96px;width:335px;font-size:11.5px;line-height:1.4}
.services{position:absolute;left:18px;top:178px;width:170px;font-size:11.5px;line-height:1.4}
.services .accent{color:var(--yellow);font-weight:700}
.service-list{list-style:none;margin-top:14px}
.service-list li{position:relative;padding-left:24px;margin-bottom:9px}
.service-photo{position:absolute;left:200px;top:180px;width:155px;height:228px;border-radius:18px;background:var(--photo-meadow)}
.care-band{position:absolute;left:0;top:422px;width:370px;height:112px;background:var(--yellow);color:var(--paper);text-align:center;padding:12px 14px 0}
.care-band p{font-size:11.5px;font-weight:700;line-height:1.35}
.care-band .motto{font-family:"Baloo 2",sans-serif;font-size:15px;line-height:1.15;margin-top:6px}
.appointments{position:absolute;left:18px;top:544px;width:340px;font-size:11.5px;line-height:1.4}
.appointments strong{font-weight:700}
.bottom-photo{position:absolute;left:0;top:606px;width:186px;height:184px;border-radius:0 22px 0 0;background:var(--photo-grass)}
.brand{position:absolute;left:204px;top:620px;width:150px;text-align:center;font-size:13px;font-weight:600;color:var(--yellow);line-height:1.25}
.brand::before{content:"";display:block;width:14px;height:14px;border-radius:50%;background:var(--yellow);margin:0 auto 5px}
.contact-box{position:absolute;left:172px;top:694px;width:186px;height:76px;background:var(--yellow);color:var(--paper);font-family:"Baloo 2",sans-serif;font-weight:600;font-size:12.5px;line-height:1.55;padding:8px 0 0 18px}
</style>
</head>
<body>

<svg width="0" height="0" style="position:absolute">
  <defs>
    <symbol id="tick" viewBox="0 0 20 20">
      <circle cx="9" cy="11" r="7.5" fill="none" stroke="#f0b323" stroke-width="1.8"/>
      <path d="M5 10.5l3.5 3.5L18 3" fill="none" stroke="#f0b323" stroke-width="2.2" stroke-linecap="round" stroke-linejoin="round"/>
    </symbol>
  </defs>
</svg>

<article class="flyer flyer--front">
  <div class="front-photo-fill" role="img" aria-label="Foto: Therapeutin streichelt ein braunes Pferd vor einer Holzscheune"></div>
  <svg class="front-shapes" viewBox="0 0 370 790" width="370" height="790" aria-hidden="true">
    <polygon points="0,310 370,233 370,240 0,318" fill="#f0b323"/>
    <polygon points="0,790 370,700 370,712 30,790" fill="#f0b323"/>
  </svg>
  <div class="name-box heading">
    <div class="name">Lotte Brenner</div>
    <div class="role">Tierphysiotherapie<br>und Osteopathie</div>
  </div>
  <h2 class="wish-title heading">Sie möchten:</h2>
  <ul class="wish-list">
    <li><svg class="tick"><use href="#tick"/></svg>Ihrem Jungtier einen guten Start ins Leben ermöglichen?</li>
    <li><svg class="tick"><use href="#tick"/></svg>Ihr Tier langfristig fit erhalten, um bis ins hohe Alter viel Freude an gemeinsamen Unternehmungen zu haben?</li>
    <li><svg class="tick"><use href="#tick"/></svg>bei Beschwerden im Bewegungsapparat wie z.B. Hüftdysplasie, Bandscheibenvorfällen oder neurologischen Einschränkungen, nach Verletzungen oder Operationen kompetent und mit Feingefühl unterstützt werden?</li>
    <li><svg class="tick"><use href="#tick"/></svg>Ihren Sportler professionell begleiten lassen?</li>
    <li><svg class="tick"><use href="#tick"/></svg>Durch regelmäßigen Check Up, frühzeitig erkennen, ob doch mal was zwickt oder klemmt</li>
  </ul>
  <p class="closing heading">Dann sind Sie<br>bei mir genau<br>Richtig!</p>
</article>

<article class="flyer flyer--back">
  <h1 class="intro-bar heading">Ich heiße Lotte Brenner und bin Physiotherapeutin und Osteopathin für Tiere</h1>
  <p class="intro-text">Einschränkungen, Blockaden oder Schmerzen können viele Ursachen haben und äußern sich bei jedem Tier anders. Ihr Tier ist einzigartig, deshalb bekommen Sie bei mir die Behandlung, die zu Ihrem Tier und Ihnen passt!</p>
  <div class="services">
    <p>Neben der Arbeit mit meinen Händen biete ich unterschiedliche <span class="accent">Therapieformen und Leistungen</span> an wie z.b.</p>
    <ul class="service-list">
      <li><svg class="tick"><use href="#tick"/></svg>Lasertherapie</li>
      <li><svg class="tick"><use href="#tick"/></svg>Neurostim</li>
      <li><svg class="tick"><use href="#tick"/></svg>aktives und passives Bewegungstraining,</li>
      <li><svg class="tick"><use href="#tick"/></svg>gezielter Muskelaufbau</li>
      <li><svg class="tick"><use href="#tick"/></svg>und vieles mehr</li>
    </ul>
  </div>
  <div class="service-photo" role="img" aria-label="Foto: Therapeutin behandelt das Vorderbein eines Haflingers auf einer Wiese"></div>
  <section class="care-band">
    <p>Ich gehe ganz besonders auf die speziellen Bedürfnisse Ihres Tiere ein. Und begleite Sie und Ihr Tier liebevoll und einfühlsam</p>
    <p class="motto">Gemeinsam finden wir den besten Weg zu mehr Bewegung und Lebensfreude!</p>
  </section>
  <p class="appointments">Termine für Hunde und Kleintiere finden nach Vereinbarung in meiner Praxis in <strong>71634 Lindenbach, Am Wiesenhang 7 statt</strong>. Ich freue mich auf Sie</p>
  <div class="bottom-photo" role="img" aria-label="Foto: Therapeutin behandelt einen Hund im Gras"></div>
  <div class="brand">Tierphysiotherapie<br>Lotte Brenner</div>
  <address class="contact-box" style="font-style:normal">
    info@tierphysio-brenner.de<br>
    0151/2047383<br>
    www.tierphysio-brenner.de
  </address>
</article>

</body>
</html>
```